Create business card using existing logo idea and create other designs for me to choose from

am looking for a creative graphic designer to design me business cards for my business would like the grey in the logo to be black aswell as adding some sort of dynamic to give it more of an edge, will provide details while will need to go on the card aswell, i would like the designer to also come up with a few other logos and create templates with details so i can decide which one i would like other than the ideas ive provided myself

double sided with the logo and company name on one side and details and smaller avatar of logo on the other

```html
<!DOCTYPE html>
<html lang="en">
<head>
<meta charset="utf-8">
<title>Brightwall Painting &amp; Decorating – Business Card</title>
<link rel="stylesheet" href="https://fonts.googleapis.com/css2?family=Source+Sans+3:wght@400;600;700&display=swap">
<style>
  :root{
    --page-bg:#e9e9e9;
    --card-white:#fbfbfb;
    --charcoal:#2f2f31;
    --charcoal-deep:#1a1a1b;
    --accent-red:#e3191d;
    --band-light:#8c8c8c;
    --band-dark:#6a6a6a;
    --band-text:#f2f2f2;
    --brand-text:#4a4a4c;
    --contact-text:#ffffff;
  }
  *{box-sizing:border-box;margin:0;padding:0}
  html,body{width:1200px;height:900px;overflow:hidden}
  body{
    background:var(--page-bg);
    font-family:"Source Sans 3",Arial,sans-serif;
    position:relative;
  }
  .business-card{
    position:absolute;left:100px;top:162px;
    width:1000px;height:576px;
    background:var(--card-white);
    box-shadow:0 10px 30px rgba(0,0,0,.18);
  }
  .contact-panel{
    position:absolute;left:0;top:0;width:477px;height:100%;
    background:var(--charcoal);
  }
  .panel-stripe{
    position:absolute;left:477px;top:0;width:12px;height:100%;
    background:var(--accent-red);
  }
  .edge-stripe{
    position:absolute;left:950px;top:0;width:8px;height:100%;
    background:var(--accent-red);
  }
  .edge-block{
    position:absolute;left:958px;top:0;width:42px;height:100%;
    background:var(--charcoal);
  }
  .name-band{
    position:absolute;left:0;top:51px;width:506px;height:120px;
    background:linear-gradient(180deg,var(--band-light),var(--band-dark));
    display:flex;align-items:flex-end;justify-content:center;
    padding-bottom:22px;
    z-index:2;
  }
  .name-band-fold{
    position:absolute;left:477px;top:171px;z-index:1;
  }
  .band-name{
    color:var(--band-text);
    font-size:24px;font-weight:400;white-space:nowrap;
  }
  .contact-list{
    position:absolute;left:30px;top:322px;list-style:none;
  }
  .contact-item{
    display:flex;align-items:center;height:42px;
    color:var(--contact-text);font-size:21px;font-weight:700;
    white-space:nowrap;
  }
  .contact-icon{width:30px;height:30px;margin-right:14px;flex:none}
  .brand-lockup{
    position:absolute;left:489px;top:330px;width:461px;
    display:flex;align-items:center;justify-content:center;gap:12px;
  }
  .brand-mark{width:16px;height:16px;background:var(--accent-red);flex:none}
  .brand-name{
    color:var(--brand-text);font-size:28px;font-weight:400;
    white-space:nowrap;line-height:1.2;
  }
</style>
</head>
<body>
  <section class="business-card" aria-label="Business card for Brightwall Painting and Decorating">
    <div class="contact-panel"></div>
    <div class="panel-stripe"></div>
    <div class="edge-stripe"></div>
    <div class="edge-block"></div>

    <div class="name-band"><span class="band-name">Brightwall Painting &amp; Decorating</span></div>
    <svg class="name-band-fold" width="29" height="14" viewBox="0 0 29 14" aria-hidden="true">
      <polygon points="0,0 29,0 0,14" fill="var(--charcoal-deep)"/>
    </svg>

    <ul class="contact-list">
      <li class="contact-item">
        <svg class="contact-icon" viewBox="0 0 30 30" aria-hidden="true">
          <circle cx="15" cy="15" r="13" fill="var(--accent-red)"/>
          <g fill="none" stroke="#fff" stroke-width="1.8">
            <circle cx="15" cy="15" r="8"/>
            <ellipse cx="15" cy="15" rx="3.6" ry="8"/>
            <line x1="7" y1="15" x2="23" y2="15"/>
          </g>
        </svg>www.brightwallpaint.ca
      </li>
      <li class="contact-item">
        <svg class="contact-icon" viewBox="0 0 30 30" aria-hidden="true">
          <circle cx="15" cy="15" r="13" fill="var(--accent-red)"/>
          <rect x="8" y="10" width="14" height="10" fill="none" stroke="#fff" stroke-width="1.8"/>
          <polyline points="8,10 15,16 22,10" fill="none" stroke="#fff" stroke-width="1.8"/>
        </svg>dana.morrow@brightwallpaint.ca
      </li>
      <li class="contact-item">
        <svg class="contact-icon" viewBox="0 0 30 30" aria-hidden="true">
          <path d="M9 5c2 0 3 4 3 5s-2 2-2 3c1 3 4 6 7 7 1 0 2-2 3-2s5 1 5 3-3 4-5 4C13 25 5 17 5 9c0-2 2-4 4-4z" fill="var(--accent-red)"/>
        </svg>555-214-3380
      </li>
      <li class="contact-item">
        <svg class="contact-icon" viewBox="0 0 30 30" aria-hidden="true">
          <path d="M4 12c0-4 6-6 11-6s11 2 11 6v2h-6v-3h-10v3H4z" fill="var(--accent-red)"/>
          <path d="M8 16h14l2 9H6z" fill="var(--accent-red)"/>
          <circle cx="15" cy="20" r="2.6" fill="var(--charcoal)"/>
        </svg>555-630-7192
      </li>
    </ul>

    <div class="brand-lockup">
      <span class="brand-mark"></span>
      <span class="brand-name">Brightwall Painting &amp; Decorating</span>
    </div>
  </section>
</body>
</html>
```